Dale Morven Broker owner of Real Estate Company

Dale Morven, GRI CRS ABR
Broker Owner
555-318-4627
dalemorven@dalemorvenrealtors.example
47362 Larchmont Ave. Lakeview Harbor, MI 48990
Licensed in Michigan and Florida
"37 Years of Outstanding Service based on a Result Driven Marketing Plan"

```html
<!DOCTYPE html>
<html lang="en">
<head>
<meta charset="UTF-8">
<title>Dale Morven – Business Card</title>
<link href="https://fonts.googleapis.com/css2?family=Montserrat:wght@400;500;700;800&family=Oswald:wght@500;600&display=swap" rel="stylesheet">
<style>
  :root{
    --navy:#0b2d63;
    --red:#c8202a;
    --ink:#2a2a2e;
    --paper:#ffffff;
    --stage:#e9eaec;
  }
  *{box-sizing:border-box;margin:0;padding:0}
  html,body{width:1200px;height:1200px;overflow:hidden;background:var(--stage)}
  body{font-family:"Montserrat",sans-serif;position:relative}
  .card{position:absolute;left:170px;width:860px;height:510px;border-radius:44px;overflow:hidden}
  .card-front{top:50px;background:var(--paper);box-shadow:0 6px 24px rgba(0,0,0,.12)}
  .card-back{top:640px;background:var(--navy);box-shadow:0 6px 24px rgba(0,0,0,.18)}

  .brand{position:absolute;left:70px;top:66px;display:flex;align-items:center;gap:14px}
  .brand-mark{width:22px;height:22px;background:var(--red)}
  .brand-name{font-weight:800;font-size:40px;letter-spacing:1px;color:var(--navy);text-transform:uppercase;white-space:nowrap}

  .contact{position:absolute;left:70px;top:160px;color:var(--ink);font-size:18px;line-height:1.25}
  .licence{margin-bottom:12px}
  .contact-row{display:flex;align-items:flex-start;gap:14px;margin-bottom:8px;white-space:nowrap}
  .contact-row svg{flex:0 0 20px;margin-top:1px}

  .portrait{position:absolute;right:110px;top:56px;width:186px;height:186px;border-radius:50%;
    border:4px solid var(--navy);background:radial-gradient(circle at 50% 40%,#b8a38c 0%,#6f6a5c 55%,#3e4250 100%)}
  .title-block{position:absolute;right:70px;top:285px;text-align:right;text-transform:uppercase;white-space:nowrap}
  .agent-name{font-size:21px;font-weight:700;color:var(--navy)}
  .agent-name .creds{font-weight:500;color:var(--ink)}
  .agent-role{font-size:18px;font-weight:500;color:var(--ink);margin-top:4px}

  .rule{position:absolute;left:0;right:0;top:386px;height:9px;background:var(--navy)}
  .tagline-band{position:absolute;left:0;right:0;top:402px;height:54px;background:var(--navy);
    display:flex;align-items:center;justify-content:center;color:#fff;white-space:nowrap;
    font-family:"Oswald",sans-serif;font-weight:600;font-size:23px;letter-spacing:.3px;text-transform:uppercase}

  .back-brand{position:absolute;inset:0;display:flex;align-items:center;justify-content:center;gap:22px}
  .back-brand .brand-mark{width:34px;height:34px}
  .back-brand .brand-name{color:#fff;font-size:72px}
</style>
</head>
<body>
  <section class="card card-front">
    <div class="brand">
      <span class="brand-mark"></span>
      <span class="brand-name">Dale Morven</span>
    </div>

    <div class="contact">
      <p class="licence">Licensed in Michigan and Florida</p>
      <div class="contact-row">
        <svg width="20" height="20" viewBox="0 0 24 24" fill="#0b2d63"><path d="M6.6 10.8a15.1 15.1 0 0 0 6.6 6.6l2.2-2.2c.3-.3.7-.4 1-.2 1.1.4 2.3.6 3.6.6.6 0 1 .4 1 1V20c0 .6-.4 1-1 1A17 17 0 0 1 3 4c0-.6.4-1 1-1h3.5c.6 0 1 .4 1 1 0 1.3.2 2.5.6 3.6.1.3 0 .7-.2 1z"/></svg>
        <span>555-318-4627</span>
      </div>
      <div class="contact-row">
        <svg width="20" height="20" viewBox="0 0 24 24" fill="#0b2d63"><path d="M2 5h20v14H2z"/><path d="M2 5l10 8 10-8" fill="none" stroke="#fff" stroke-width="1.8"/></svg>
        <span>dalemorven@dalemorvenrealtors.example</span>
      </div>
      <div class="contact-row">
        <svg width="20" height="20" viewBox="0 0 24 24" fill="#0b2d63"><path d="M12 2a7 7 0 0 0-7 7c0 5 7 13 7 13s7-8 7-13a7 7 0 0 0-7-7zm0 9.5A2.5 2.5 0 1 1 12 6.5a2.5 2.5 0 0 1 0 5z"/></svg>
        <span>47362 Larchmont Ave.<br>Lakeview Harbor, MI 48990</span>
      </div>
    </div>

    <div class="portrait" role="img" aria-label="Portrait photograph of Dale Morven"></div>

    <div class="title-block">
      <p class="agent-name">Dale Morven <span class="creds">| GRI CRS ABR</span></p>
      <p class="agent-role">Broker Owner</p>
    </div>

    <div class="rule"></div>
    <div class="tagline-band">37 Years of Outstanding Service Based on a Result Driven Marketing Plan</div>
  </section>

  <section class="card card-back">
    <div class="back-brand">
      <span class="brand-mark"></span>
      <span class="brand-name">Dale Morven</span>
    </div>
  </section>
</body>
</html>
```